Tea standup pouch labels

Dear designers,
I need a minimalistic and modern label for my loose tea stand-up pouches (100, 250 and 500gm packs). The label should cover 70-80% of the pouch face (front and rear both).
The label will be 2 part label - Front and Rear side labels.
The labels should have a green background (Pantone Green C) with Golden or White or black colour text. Please either use the Golden logo or black logo to see which looks good with Pantone Green C background.
I am also attaching the content file and a few other files (Assam tea logo) to be used in the label.
The Assam tea logo should be small at the bottom left or right side of the front side. The logo should be dominant on the front page (some of the designs I received have small logo and big "100% single estate tea" and "Assam logo" as big characters on the front page which is not what I am looking for.

The font style should note simple Times new roman or Arial. It should look modern and should be something matching to the logo sentence 'Freshest possible' but should also not be in italics. Please refer to files Font style reference front and back for the style of font. Also use the same box space design on the rear - Content should be in White background; the rectangular box edges should be rounded and the border should be in dual colour - Golden and white or in black and white depending on the logo colour used (golden or black).

For the Rear page - headings could be in Golden colour or black colour depending on the logo colour you choose to use and the text can be in white colour i.e. Option 1 - Headings in golden colour and text in white colour; Option 2 - Heading in Black colour and text in white colour or any other combination that looks good - designer to decide.

Please let me know if you need any further information.

thanks,
Dorin

33b8a4

```html
<!DOCTYPE html>
<html lang="en">
<head>
<meta charset="utf-8">
<title>Brewhaven – Single Estate Tea Label</title>
<link rel="stylesheet" href="https://fonts.googleapis.com/css2?family=Josefin+Sans:wght@400;600&family=Dancing+Script:wght@500&display=swap">
<style>
  :root {
    --canvas-bg: #e4efee;
    --label-cream: #f4efe9;
    --pattern-tone: #ebe5de;
    --gold: #a27b2c;
    --estate-green: #138456;
    --white: #ffffff;
    --ink-dark: #2b2b2b;
  }
  * { box-sizing: border-box; margin: 0; padding: 0; }
  html, body {
    width: 1200px;
    height: 1200px;
    overflow: hidden;
    background: var(--canvas-bg);
  }
  .label {
    position: absolute;
    left: 254px;
    top: 50px;
    width: 692px;
    height: 1100px;
    background: var(--label-cream);
    overflow: hidden;
    font-family: "Josefin Sans", sans-serif;
  }
  .leaf-pattern {
    position: absolute;
    inset: 0 0 240px 0;
    background: radial-gradient(ellipse at 50% 45%, var(--label-cream) 0%, var(--pattern-tone) 100%);
  }
  .estate-heading {
    position: absolute;
    top: 150px;
    width: 100%;
    text-align: center;
    color: var(--gold);
    font-weight: 600;
    font-size: 47px;
    line-height: 58px;
    letter-spacing: 2px;
  }
  .brand-lockup {
    position: absolute;
    top: 430px;
    width: 100%;
    display: flex;
    flex-direction: column;
    align-items: center;
    gap: 40px;
  }
  .brand-mark {
    width: 84px;
    height: 84px;
    border: 5px solid var(--gold);
    border-radius: 50%;
  }
  .brand-name {
    color: var(--gold);
    font-weight: 400;
    font-size: 78px;
    letter-spacing: 14px;
    padding-left: 14px;
  }
  .tagline {
    position: absolute;
    top: 760px;
    width: 100%;
    text-align: center;
    color: var(--gold);
    font-family: "Dancing Script", cursive;
    font-size: 34px;
  }
  .green-band {
    position: absolute;
    left: 0;
    bottom: 0;
    width: 692px;
    height: 270px;
  }
  .net-weight {
    position: absolute;
    top: 960px;
    left: 226px;
    width: 260px;
    text-align: center;
    color: var(--white);
    font-family: "Josefin Sans", sans-serif;
    font-size: 29px;
    line-height: 44px;
    letter-spacing: 1px;
  }
  .origin-badge {
    position: absolute;
    left: 504px;
    top: 918px;
    width: 130px;
    height: 130px;
    border-radius: 50%;
    background: var(--white);
    border: 4px solid var(--ink-dark);
  }
</style>
</head>
<body>
  <main class="label">
    <div class="leaf-pattern" role="img" aria-label="Faint pattern of line-drawn tea leaves and sprigs"></div>

    <h1 class="estate-heading">100% SINGLE<br>ESTATE TEA</h1>

    <div class="brand-lockup">
      <span class="brand-mark"></span>
      <span class="brand-name">BREWHAVEN</span>
    </div>

    <p class="tagline">freshest possible</p>

    <svg class="green-band" viewBox="0 0 692 270" aria-hidden="true">
      <path fill="var(--estate-green)" d="M0 18 L18 8 L30 20 L48 4 L62 16 L80 6 L96 22 L112 10 L130 18 L150 2 L166 16 L184 8 L200 24 L218 10 L236 18 L254 4 L272 20 L290 8 L308 16 L326 2 L344 18 L362 10 L380 22 L398 6 L416 18 L434 10 L452 24 L470 8 L488 16 L506 2 L524 20 L542 10 L560 18 L578 4 L596 20 L614 8 L632 18 L650 6 L668 20 L692 10 L692 270 L0 270 Z"/>
    </svg>

    <p class="net-weight">Net Wt<br>250g/8.82oz</p>

    <div class="origin-badge" role="img" aria-label="Regional origin certification badge"></div>
  </main>
</body>
</html>
```